Visitenkarten
Zielgruppe
Wir begleiten dich in der Ausbildung, im Studium, bei der Fachwirt-Weiterbildung, damit du deine Prüfungen ohne Hindernisse erfolgreich meisterst.
Aufgabenstellung
Auf der Visitenkarte muss das Logo und folgende Informationen zu sehen sein:
Lernwerkcoach
Timo Brandau
Quaderweg Str. 58
04388 Leipzig
Telefon: 0152 - 3208947
E-Mail: info@lernwerkcoach-beispiel.de
Homepage: www.lernwerkcoach-beispiel.de
sowie einen Link zu meinem Terminvereinbarungskalender: www.terminfix-beispiel.de/lernwerkcoach mit dem Hinweis: „Hier Termin vereinbaren“ (sinngemäße Abwandlung möglich).
Es muss auch ein Hinweis auf eine kostenfreie Probestunde drauf.

```html
<!DOCTYPE html>
<html lang="de">
<head>
<meta charset="utf-8">
<title>Visitenkarte Lernwerkcoach</title>
<link rel="stylesheet" href="https://fonts.googleapis.com/css2?family=Montserrat:wght@600;700&family=Open+Sans:wght@400;600;700&display=swap">
<style>
  :root {
    --teal: #1f5857;
    --teal-dark: #17464a;
    --paper: #f4f5f5;
    --ink: #2e3436;
    --white: #ffffff;
    --backdrop: #e4e6e7;
  }
  * { margin: 0; padding: 0; box-sizing: border-box; }
  html, body { width: 1200px; height: 720px; overflow: hidden; }
  body {
    background: var(--backdrop);
    font-family: "Open Sans", Arial, sans-serif;
    position: relative;
  }
  .card {
    position: absolute;
    top: 185px;
    width: 540px;
    height: 350px;
    overflow: hidden;
    box-shadow: 0 6px 18px rgba(0,0,0,0.14);
  }
  .card--back { left: 40px; background: var(--paper); }
  .card--front { left: 620px; background: var(--teal); }

  .card__shapes { position: absolute; inset: 0; }

  .person { position: absolute; right: 28px; top: 16px; text-align: right; color: var(--white); }
  .person__name { font-family: "Montserrat", Arial, sans-serif; font-weight: 700; font-size: 30px; line-height: 1.1; }
  .person__role { font-size: 13px; letter-spacing: 0.6px; text-transform: uppercase; }

  .wordmark-block { position: absolute; left: 28px; top: 168px; display: flex; align-items: center; gap: 10px; }
  .wordmark-block__square { width: 22px; height: 22px; background: var(--teal); }
  .wordmark { font-family: "Montserrat", Arial, sans-serif; font-weight: 700; font-size: 25px; color: var(--teal); }

  .trial { position: absolute; left: 28px; top: 226px; color: var(--teal); line-height: 1.35; }
  .trial__title { font-family: "Montserrat", Arial, sans-serif; font-weight: 700; font-size: 15px; text-transform: uppercase; letter-spacing: 0.4px; }
  .trial__hint { font-size: 13px; font-weight: 600; color: var(--ink); }

  .contact { position: absolute; left: 292px; top: 120px; list-style: none; color: var(--ink); font-size: 14.5px; }
  .contact__item { display: flex; align-items: flex-start; gap: 10px; line-height: 1.3; margin-bottom: 7px; }
  .contact__icon { width: 16px; height: 16px; flex: none; margin-top: 2px; }

  .booking { position: absolute; left: 0; right: 0; bottom: 0; height: 52px; display: flex; align-items: center; padding-left: 26px; color: var(--white); font-size: 13.5px; white-space: nowrap; }
  .booking__url { font-weight: 600; margin-left: 5px; }

  .brand { position: absolute; inset: 0; display: flex; flex-direction: column; align-items: center; justify-content: center; color: var(--white); text-align: center; }
  .brand__row { display: flex; align-items: center; gap: 14px; }
  .brand__square { width: 34px; height: 34px; background: var(--white); }
  .brand__name { font-family: "Montserrat", Arial, sans-serif; font-weight: 700; font-size: 44px; }
  .brand__claim { margin-top: 12px; font-size: 11.5px; letter-spacing: 1px; text-transform: uppercase; line-height: 1.4; }
</style>
</head>
<body>

<section class="card card--back" aria-label="Visitenkarte Rückseite">
  <svg class="card__shapes" width="540" height="350" viewBox="0 0 540 350" aria-hidden="true">
    <polygon points="250,0 540,0 540,92 300,92 140,130" fill="var(--teal)"/>
    <rect x="300" y="284" width="240" height="8" fill="var(--teal)"/>
    <rect x="0" y="298" width="540" height="52" fill="var(--teal)"/>
  </svg>

  <header class="person">
    <h1 class="person__name">Timo Brandau</h1>
    <p class="person__role">Lernwerkcoach</p>
  </header>

  <div class="wordmark-block">
    <span class="wordmark-block__square"></span>
    <span class="wordmark">Lernwerkcoach</span>
  </div>

  <div class="trial">
    <p class="trial__title">Kostenfreie Probestunde</p>
    <p class="trial__hint">Hier Termin vereinbaren:</p>
  </div>

  <ul class="contact">
    <li class="contact__item">
      <svg class="contact__icon" viewBox="0 0 16 16" aria-hidden="true"><path d="M8 1.5a4.5 4.5 0 0 0-4.5 4.5c0 3.4 4.5 8.5 4.5 8.5s4.5-5.1 4.5-8.5A4.5 4.5 0 0 0 8 1.5z" fill="none" stroke="var(--ink)" stroke-width="1.4"/><circle cx="8" cy="6" r="1.6" fill="var(--ink)"/></svg>
      <span>Quaderweg Str. 58<br>04388 Leipzig</span>
    </li>
    <li class="contact__item">
      <svg class="contact__icon" viewBox="0 0 16 16" aria-hidden="true"><path d="M3.5 1.5l2.5 3-1.5 1.5c.8 2 2.5 3.7 4.5 4.5l1.5-1.5 3 2.5-1.5 2.5C7 14 2 9 1 3z" fill="var(--ink)"/></svg>
      <span>0152 - 3208947</span>
    </li>
    <li class="contact__item">
      <svg class="contact__icon" viewBox="0 0 16 16" aria-hidden="true"><rect x="1.5" y="3.5" width="13" height="9" fill="none" stroke="var(--ink)" stroke-width="1.4"/><path d="M1.5 3.5L8 9l6.5-5.5" fill="none" stroke="var(--ink)" stroke-width="1.4"/></svg>
      <span>info@lernwerkcoach-beispiel.de</span>
    </li>
    <li class="contact__item">
      <svg class="contact__icon" viewBox="0 0 16 16" aria-hidden="true"><circle cx="8" cy="8" r="6.5" fill="none" stroke="var(--ink)" stroke-width="1.3"/><ellipse cx="8" cy="8" rx="2.8" ry="6.5" fill="none" stroke="var(--ink)" stroke-width="1.1"/><path d="M1.5 8h13M2.5 4.8h11M2.5 11.2h11" stroke="var(--ink)" stroke-width="1"/></svg>
      <span>www.lernwerkcoach-beispiel.de</span>
    </li>
  </ul>

  <p class="booking">Terminvereinbarungskalender :<span class="booking__url">www.terminfix-beispiel.de/lernwerkcoach</span></p>
</section>

<section class="card card--front" aria-label="Visitenkarte Vorderseite">
  <div class="brand">
    <div class="brand__row">
      <span class="brand__square"></span>
      <span class="brand__name">Lernwerkcoach</span>
    </div>
    <p class="brand__claim">Weiterbildungsinstitut für Rechnungswesen,<br>Wirtschaftslehre und Steuerrecht</p>
  </div>
</section>

</body>
</html>
```